School Hallway Magnetic Display Design for school values

I am looking for a someone to help me design a magnetic hallway display that will hang in the hallway of our small school. There are several elements, including 1. 6ft by 4ft designed magnetic bulletin board, 2. Magnets that will stick to the board. See attachment for which elements belong where. The display will be for our TRAVEK program, which rewards students for demonstrating our school values. We want the display to be beautiful and interactive. We are also rebranding, so we want the design to align with our new fonts and colors. In the attached PDF is an outline of our new brand guidelines. Unfortunately, we don't have the color codes, but I'm hoping that you can match the colors listed. Attached are elements to be used on the board, but please use your creativity to make it more dynamic and visually appealing. For example, the star magnets could be another shape. The TRAVEK magnets must remain the same. I've included two photos of boards at other schools that inspired this project.

Target Market(s)

School Community

Industry/Entity Type

Education

Requirements
Should not have
• School Logo

```html
<!DOCTYPE html>
<html lang="en">
<head>
<meta charset="utf-8">
<title>TRAVEK Reward Program Board</title>
<link rel="stylesheet" href="https://fonts.googleapis.com/css2?family=Fredoka:wght@600;700&family=Montserrat:wght@600;700;800;900&display=swap">
<style>
  :root {
    --navy: #1d3565;
    --navy-deep: #16294f;
    --red: #df302d;
    --orange: #ee7a22;
    --yellow: #f2b51c;
    --teal: #1f9e92;
    --blue: #1f78b8;
    --indigo: #2b3f8f;
    --green: #7ab53f;
    --paper: #ffffff;
    --ink: #1b2440;
  }
  * { box-sizing: border-box; margin: 0; padding: 0; }
  html, body { width: 1200px; height: 805px; overflow: hidden; background: var(--paper); }
  body { font-family: "Montserrat", Arial, sans-serif; color: var(--ink); position: relative; }

  .board-header {
    position: absolute; left: 0; top: 0; width: 1200px; height: 104px;
    background: var(--navy); border-bottom: 6px solid var(--green);
  }
  .ribbons { position: absolute; left: 28px; top: 0; display: flex; gap: 8px; }
  .ribbon { width: 46px; height: 86px; }
  .board-title {
    position: absolute; left: 0; right: 0; top: 26px; text-align: center;
    color: var(--paper); font-weight: 800; font-size: 44px; letter-spacing: 1px;
  }
  .school-name {
    position: absolute; right: 28px; top: 34px; height: 32px;
    display: flex; align-items: center; gap: 10px;
    color: var(--paper); font-weight: 800; font-size: 22px; letter-spacing: .5px;
  }
  .school-name .mark { width: 26px; height: 26px; background: var(--green); }

  .acronym, .value-columns {
    position: absolute; left: 40px; width: 1120px;
    display: grid; grid-template-columns: repeat(6, 1fr); gap: 16px;
  }
  .acronym { top: 112px; height: 130px; }
  .acronym span {
    text-align: center; font-family: "Fredoka", Arial, sans-serif; font-weight: 700; font-size: 120px; line-height: 130px;
    text-shadow: -3px -3px 0 #fff, 3px -3px 0 #fff, -3px 3px 0 #fff, 3px 3px 0 #fff, 4px 6px 6px rgba(0,0,0,.3);
  }

  .value-columns { top: 252px; height: 336px; }
  .value-card {
    border: 3px solid var(--c); border-radius: 10px; background: var(--paper);
    display: flex; flex-direction: column; overflow: hidden; position: relative;
  }
  .value-card h2 {
    background: var(--c); color: var(--paper); font-weight: 800; font-size: 18px;
    text-align: center; padding: 8px 0; letter-spacing: .5px;
  }
  .icon-art {
    margin: 12px 14px 0; height: 196px; border-radius: 8px;
    background: linear-gradient(160deg, var(--c) 0%, color-mix(in srgb, var(--c) 45%, #fff) 100%); opacity: .35;
  }
  .badges { display: flex; justify-content: center; gap: 6px; margin-top: 10px; height: 52px; }
  .badge {
    width: 50px; height: 50px; border-radius: 50%; border: 4px solid var(--c); background: var(--paper);
    display: flex; align-items: center; justify-content: center; text-align: center;
    font-size: 7px; font-weight: 800; line-height: 1.15; color: var(--c);
  }
  .value-label {
    margin-top: auto; padding-bottom: 8px; text-align: center;
    font-family: "Fredoka", Arial, sans-serif; font-weight: 700; font-size: 22px; color: var(--ink);
  }
  .name-magnet {
    position: absolute; width: 44px; height: 44px; border-radius: 50%;
    background: var(--navy); color: var(--paper); border: 2px solid #fff;
    display: flex; align-items: center; justify-content: center; text-align: center;
    font-size: 10px; font-weight: 700; line-height: 1.1; box-shadow: 0 2px 4px rgba(0,0,0,.3);
  }

  .info-band {
    position: absolute; left: 0; top: 600px; width: 1200px; height: 205px;
    background: var(--navy); border-top: 6px solid var(--green);
    display: grid; grid-template-columns: 1fr 1fr; gap: 28px; padding: 12px 40px 14px;
  }
  .info-panel { display: flex; flex-direction: column; }
  .info-panel h3 {
    color: var(--paper); font-weight: 800; font-size: 20px; text-align: center;
    padding: 8px 0; background: var(--navy-deep); border-radius: 6px 6px 0 0;
  }
  .info-body { flex: 1; padding: 10px 16px; color: var(--paper); font-size: 12.5px; line-height: 1.45; font-weight: 600; border-radius: 0 0 6px 6px; }
  .definitions .info-body { background: var(--orange); color: var(--ink); }
  .definitions strong { font-weight: 800; }
  .earn .info-body { background: var(--teal); }
  .earn ul { list-style: none; }
  .earn li::before { content: "• "; font-weight: 800; }
</style>
</head>
<body>
  <header class="board-header">
    <div class="ribbons">
      <svg class="ribbon" viewBox="0 0 46 86"><path d="M0 0H46V86L23 70L0 86Z" fill="#df302d"/></svg>
      <svg class="ribbon" viewBox="0 0 46 86"><path d="M0 0H46V86L23 70L0 86Z" fill="#f2b51c"/></svg>
      <svg class="ribbon" viewBox="0 0 46 86"><path d="M0 0H46V86L23 70L0 86Z" fill="#1f78b8"/></svg>
    </div>
    <h1 class="board-title">TRAVEK REWARD PROGRAM</h1>
    <div class="school-name"><span class="mark"></span>TRAVEK</div>
  </header>

  <div class="acronym" aria-label="TRAVEK">
    <span style="color: var(--red)">T</span>
    <span style="color: var(--orange)">R</span>
    <span style="color: var(--yellow)">A</span>
    <span style="color: var(--teal)">V</span>
    <span style="color: var(--blue)">E</span>
    <span style="color: var(--indigo)">K</span>
  </div>

  <section class="value-columns">
    <article class="value-card" style="--c: var(--red)">
      <h2>SPIRIT</h2>
      <div class="icon-art" role="img" aria-label="Rocket magnets"></div>
      <div class="badges"><div class="badge">STUDENT ACHIEVER</div><div class="badge">STUDENT ACHIEVER</div></div>
      <p class="value-label">Spirit</p>
    </article>
    <article class="value-card" style="--c: var(--orange)">
      <h2>POTENTIAL</h2>
      <div class="icon-art" role="img" aria-label="Seedling magnets"></div>
      <div class="badges"><div class="badge">STUDENT ACHIEVER</div><div class="badge">STUDENT ACHIEVER</div></div>
      <p class="value-label">Potential</p>
    </article>
    <article class="value-card" style="--c: var(--yellow)">
      <h2>INNOVATION</h2>
      <div class="icon-art" role="img" aria-label="Light bulb and gear magnets"></div>
      <div class="badges"><div class="badge">STUDENT ACHIEVER</div></div>
      <p class="value-label">Innovation</p>
    </article>
    <article class="value-card" style="--c: var(--teal)">
      <h2>CURIOSITY</h2>
      <div class="icon-art" role="img" aria-label="Telescope and compass magnets"></div>
      <div class="name-magnet" style="left: 14px; top: 112px">Lena K.</div>
      <div class="badges"><div class="badge">STUDENT ACHIEVER</div><div class="badge">STUDENT ACHIEVER</div></div>
      <p class="value-label">Curiosity</p>
    </article>
    <article class="value-card" style="--c: var(--blue)">
      <h2>ETHICS</h2>
      <div class="icon-art" role="img" aria-label="Scale and handshake magnets"></div>
      <div class="name-magnet" style="right: 12px; top: 100px">Maya T.</div>
      <div class="name-magnet" style="right: 12px; top: 236px">Maya T.</div>
      <div class="badges"></div>
      <p class="value-label">Ethics</p>
    </article>
    <article class="value-card" style="--c: var(--indigo)">
      <h2>SYNERGY</h2>
      <div class="icon-art" role="img" aria-label="Team and puzzle piece magnets"></div>
      <div class="name-magnet" style="right: 12px; top: 50px">Jonah R.</div>
      <div class="badges"></div>
      <p class="value-label">Synergy</p>
    </article>
  </section>

  <section class="info-band">
    <div class="info-panel definitions">
      <h3>TRAVEK VALUE DEFINITIONS</h3>
      <div class="info-body">
        <p><strong>Spirit</strong> – Bringing energy, pride and kindness to our school every single day.</p>
        <p><strong>Potential</strong> – Growing through effort, practice and patience to reach new goals.</p>
        <p><strong>Innovation</strong> – Trying fresh ideas and creative ways to solve problems.</p>
        <p><strong>Synergy</strong> – Working as a team, sharing ideas, helping others and listening.</p>
      </div>
    </div>
    <div class="info-panel earn">
      <h3>HOW STUDENTS EARN TRAVEK</h3>
      <div class="info-body">
        <ul>
          <li>Show one of our values in class or around the school.</li>
          <li>A teacher notices the action and hands you a value magnet.</li>
          <li>Place your magnet in the matching column on the board.</li>
          <li>Collect magnets from every value to earn a special reward.</li>
          <li>Help a classmate reach their goal and earn bonus points.</li>
          <li>Read your name at the monthly recognition assembly.</li>
        </ul>
      </div>
    </div>
  </section>
</body>
</html>
```